Flyer Design Project

We would like a double sided a5 flyer. To promote our new brand which is velvetine mobile, attached is the logo. This is for a mobile telecom company.
The aim of the flyer is to create brand awareness, to pormote a managed service for mobile phone connections/ tariffs. For business users and also personal use.

We would like to focus to be on offshore billing and discrete billing for users based abroad. eg students

Theme should be based around Plumleaf and Zorphones , one side should focus on business users and the other should focus on personal use. The focus on business users should be based around , Virtual landline numbers, where users can have a landline number connected to their mobile phones.
Should be elegant, up class ,and not to much text bullet points would be good .

Branding of telecoms QX ,K7 ,Telmarix,.
Updates

Velvetine mobile

Contact info for the flyer. 
info@velvetinemobile.example
www.velvetinemobile.example
0871 463 19 19 

Flyers need to look elegant and good creative designs please.

Industry/Entity Type

Telecom

```html
<!DOCTYPE html>
<html lang="en">
<head>
<meta charset="utf-8">
<title>Velvetine Mobile — A5 Flyer</title>
<link rel="stylesheet" href="https://fonts.googleapis.com/css2?family=Tinos:ital,wght@0,400;0,700;1,700&display=swap">
<style>
  :root {
    --page-bg: #e4e4e4;
    --flyer-black: #050608;
    --flyer-navy: #0b2a5c;
    --brand-blue: #0e5fd8;
    --brand-blue-deep: #0a49a8;
    --brand-green: #1f8f1f;
    --text-white: #ffffff;
    --text-faint: rgba(150, 170, 200, 0.28);
    --photo-silver: #c9ccd1;
    --photo-dark: #2b2f36;
  }
  * { box-sizing: border-box; margin: 0; padding: 0; }
  html, body {
    width: 1200px; height: 800px; overflow: hidden;
    background: var(--page-bg);
    font-family: "Tinos", "Times New Roman", serif;
  }
  .canvas { position: relative; width: 1200px; height: 800px; }

  .flyer {
    position: absolute; top: 202px; width: 560px; height: 396px; overflow: hidden;
    background:
      radial-gradient(ellipse at 55% 75%, var(--flyer-navy) 0%, rgba(11,42,92,0) 60%),
      var(--flyer-black);
    color: var(--text-white);
  }
  .flyer--business { left: 30px; }
  .flyer--personal { left: 610px; }

  /* Business side */
  .top-band { position: absolute; left: 0; top: 0; width: 100%; height: 16px; background: var(--brand-blue); }
  .top-band::after { content: ""; position: absolute; left: 0; top: 16px; width: 100%; height: 6px; background: var(--brand-green); }

  .deco-frame { position: absolute; left: 355px; top: 42px; width: 145px; height: 145px; background: rgba(14,95,216,0.18); }
  .deco-blue { position: absolute; left: 373px; top: 55px; width: 112px; height: 110px; background: var(--brand-blue-deep); }
  .deco-green { position: absolute; left: 290px; top: 120px; width: 112px; height: 118px; background: var(--brand-green); opacity: .85; }

  .brand { position: absolute; display: flex; align-items: center; gap: 8px; font-weight: 400; letter-spacing: .04em; text-transform: uppercase; color: var(--text-white); }
  .brand-square { width: 9px; height: 9px; background: var(--brand-green); }
  .brand--header { left: 0; width: 470px; top: 58px; justify-content: center; font-size: 15px; }
  .brand--faint { left: 40px; width: 400px; top: 318px; justify-content: center; font-size: 30px; color: var(--text-faint); }
  .brand--faint .brand-square { width: 14px; height: 14px; background: var(--text-faint); }

  .business-heading { position: absolute; left: 0; width: 470px; top: 134px; text-align: center; font-size: 15px; font-weight: 700; font-style: italic; text-transform: uppercase; }
  .feature-list { position: absolute; left: 90px; top: 168px; width: 360px; list-style: none; font-size: 12px; font-weight: 700; line-height: 1.35; }
  .feature-list li { position: relative; padding-left: 8px; margin-bottom: 20px; }
  .feature-list li::before { content: ""; position: absolute; left: 0; top: 3px; width: 7px; height: 7px; border-radius: 50%; background: var(--brand-blue); }

  /* Personal side */
  .block-green { position: absolute; left: 110px; top: 0; width: 105px; height: 70px; background: var(--brand-green); }
  .block-blue { position: absolute; left: 248px; top: 0; width: 150px; height: 152px; background: var(--brand-blue-deep); }
  .personal-headline { position: absolute; left: 0; width: 100%; top: 30px; text-align: center; font-size: 16px; font-weight: 700; line-height: 2.35; }
  .brand--center { left: 0; width: 100%; top: 238px; justify-content: center; font-size: 19px; }
  .photo { position: absolute; }
  .photo--zorphone { left: 5px; top: 185px; width: 125px; height: 170px; border-radius: 14px; background: linear-gradient(160deg, #eef0f3, var(--photo-silver) 60%, #8d9299); }
  .photo--plumleaf { left: 385px; top: 190px; width: 160px; height: 150px; border-radius: 12px; background: linear-gradient(160deg, #5a616b, var(--photo-dark) 55%, #111418); }
  .personal-footer { position: absolute; left: 0; width: 100%; top: 408px; }
  .savings-line { position: absolute; left: 0; width: 100%; top: 356px; text-align: center; font-size: 14px; font-weight: 700; }
</style>
</head>
<body>
<main class="canvas">

  <section class="flyer flyer--business" aria-label="Business side">
    <div class="top-band"></div>
    <div class="deco-frame"></div>
    <div class="deco-blue"></div>
    <div class="deco-green"></div>
    <div class="brand brand--header"><span class="brand-square"></span>Velvetine Mobile</div>
    <h2 class="business-heading">Never miss a business call again!</h2>
    <ul class="feature-list">
      <li>The complete telephone system solution for small businesses.</li>
      <li>With an impressive range of professional call handling features.</li>
      <li>Linkline Express allows small businesses to be responsive 24/7 by combining your landline and mobile calls.</li>
    </ul>
    <div class="brand brand--faint"><span class="brand-square"></span>Velvetine Mobile</div>
  </section>

  <section class="flyer flyer--personal" aria-label="Personal side">
    <div class="block-green"></div>
    <div class="block-blue"></div>
    <h1 class="personal-headline">Never miss a call again, get your landline number on your mobile.<br>Offshore and discrete billing.</h1>
    <div class="photo photo--zorphone" role="img" aria-label="Photo of a silver Zorphone smartphone"></div>
    <div class="photo photo--plumleaf" role="img" aria-label="Photo of two dark Plumleaf smartphones"></div>
    <div class="brand brand--center"><span class="brand-square"></span>Velvetine Mobile</div>
    <p class="savings-line">We will save you money of your existing mobile provider.</p>
  </section>

</main>
</body>
</html>
```